Business Card and Letterhead Design for Public Accounting Firm

Business card and letterhead design for a CPA Firm located in Orange County, CA. We're looking for a modern and professional design utilizing our existing logo. We'd like a clean "less is more" look, but also something that catches the eye. We provide a high level of service to our clients. Open to single or double sided business cards.

Additional info: color numbers on logo
Blue :
R 0
G 83
B 125

#00537D

Silver :

R 154
G 154
B 154

#9A9A9A

Target Market(s)

Businesses and individuals

Industry/Entity Type

Accounting

Contact Information for Business Card

Moss Whitfield & Danby LLP - 4827 Larkspur Vale Road, Irvine, CA 92614 - (949)731-2864 - mwdaccts.example

Font styles to use
Serif
Sans Serif
Other font styles liked:
• See font file uploaded

Colors
0054AA
0677BA
7BADD7
CADEEF
E8F1F8

Requirements
Nice to have
• Possibly use the font file provided which matches our logo, but adjust to be not in all caps

```html
<!DOCTYPE html>
<html lang="en">
<head>
<meta charset="utf-8">
<title>Moss Whitfield &amp; Danby LLP – Business Card</title>
<link href="https://fonts.googleapis.com/css2?family=Cinzel:wght@400;600&family=Montserrat:wght@400;500&display=swap" rel="stylesheet">
<style>
  :root {
    --brand-blue: #0d4469;
    --brand-blue-light: #1a5a82;
    --silver: #9a9a9a;
    --white: #ffffff;
    --page: #e9eaec;
  }
  * { box-sizing: border-box; margin: 0; padding: 0; }
  html, body { width: 1200px; height: 1200px; overflow: hidden; }
  body {
    background: var(--page);
    display: flex;
    flex-direction: column;
    align-items: center;
    justify-content: center;
    gap: 50px;
  }
  .card {
    position: relative;
    width: 900px;
    height: 520px;
    border-radius: 40px;
    overflow: hidden;
    box-shadow: 0 10px 30px rgba(0,0,0,.18);
  }

  /* Front */
  .card--front { background: var(--white); }
  .front-top {
    height: 262px;
    display: flex;
    align-items: center;
    justify-content: center;
  }
  .wordmark {
    font-family: "Cinzel", serif;
    font-weight: 600;
    letter-spacing: 2px;
  }
  .front-top .wordmark { font-size: 110px; color: var(--brand-blue); }
  .stripe { height: 12px; background: var(--silver); margin-bottom: 14px; }
  .front-bottom {
    position: absolute;
    left: 0; right: 0; bottom: 0;
    top: 288px;
    background: var(--brand-blue);
    display: flex;
    align-items: center;
    padding: 0 60px;
  }
  .firm-name {
    font-family: "Cinzel", serif;
    color: var(--white);
    font-size: 34px;
    line-height: 1.05;
    width: 330px;
  }
  .divider {
    width: 1px;
    height: 150px;
    background: rgba(255,255,255,.5);
    margin: 0 50px 0 40px;
  }
  .contact { list-style: none; font-family: "Montserrat", sans-serif; color: var(--white); font-size: 21px; }
  .contact li { display: flex; align-items: flex-start; gap: 14px; line-height: 1.3; margin: 4px 0; }
  .contact svg { width: 20px; height: 20px; flex: none; margin-top: 4px; fill: var(--white); }

  /* Back */
  .card--back {
    background: linear-gradient(100deg, var(--brand-blue) 0%, var(--brand-blue) 40%, var(--brand-blue-light) 52%, var(--brand-blue) 62%);
    display: flex;
    align-items: center;
    justify-content: center;
  }
  .card--back .wordmark { font-size: 96px; color: var(--white); }
  .back-divider { width: 1px; height: 180px; background: var(--silver); margin: 0 36px; }
  .back-name {
    font-family: "Cinzel", serif;
    color: var(--silver);
    font-size: 40px;
    letter-spacing: 6px;
    line-height: 1.15;
  }
</style>
</head>
<body>

<section class="card card--front">
  <div class="front-top"><span class="wordmark">MW&amp;D</span></div>
  <div class="stripe"></div>
  <div class="front-bottom">
    <p class="firm-name">Moss Whitfield<br>&amp; Danby LLP</p>
    <div class="divider"></div>
    <ul class="contact">
      <li>
        <svg viewBox="0 0 24 24" aria-hidden="true"><path d="M6.6 10.8a15 15 0 0 0 6.6 6.6l2.2-2.2a1 1 0 0 1 1-.25 11.4 11.4 0 0 0 3.6.57 1 1 0 0 1 1 1V20a1 1 0 0 1-1 1A17 17 0 0 1 3 4a1 1 0 0 1 1-1h3.5a1 1 0 0 1 1 1c0 1.25.2 2.45.57 3.57a1 1 0 0 1-.25 1z"/></svg>
        (949) 731-2864
      </li>
      <li>
        <svg viewBox="0 0 24 24" aria-hidden="true"><path d="M12 2a10 10 0 1 0 0 20 10 10 0 0 0 0-20zm6.9 6h-2.9a15.6 15.6 0 0 0-1.4-3.6A8 8 0 0 1 18.9 8zM12 4c.8 1.2 1.5 2.5 1.9 4h-3.8c.4-1.5 1.1-2.8 1.9-4zM4.3 14a8 8 0 0 1 0-4h3.4a16 16 0 0 0 0 4zm.8 2h2.9c.3 1.3.8 2.5 1.4 3.6A8 8 0 0 1 5.1 16zM8 8H5.1a8 8 0 0 1 4.3-3.6C8.8 5.5 8.3 6.7 8 8zm4 12c-.8-1.2-1.5-2.5-1.9-4h3.8c-.4 1.5-1.1 2.8-1.9 4zm2.3-6H9.7a14.6 14.6 0 0 1 0-4h4.6a14.6 14.6 0 0 1 0 4zm.3 5.6c.6-1.1 1.1-2.3 1.4-3.6h2.9a8 8 0 0 1-4.3 3.6zM16.3 14a16 16 0 0 0 0-4h3.4a8 8 0 0 1 0 4z"/></svg>
        mwdaccts.example
      </li>
      <li>
        <svg viewBox="0 0 24 24" aria-hidden="true"><path d="M12 2a7 7 0 0 0-7 7c0 5.2 7 13 7 13s7-7.8 7-13a7 7 0 0 0-7-7zm0 9.5a2.5 2.5 0 1 1 0-5 2.5 2.5 0 0 1 0 5z"/></svg>
        <span>4827 Larkspur Vale Road<br>Irvine, CA 92614</span>
      </li>
    </ul>
  </div>
</section>

<section class="card card--back">
  <span class="wordmark">MW&amp;D</span>
  <div class="back-divider"></div>
  <p class="back-name">Moss Whitfield<br>&amp; Danby LLP</p>
</section>

</body>
</html>
```